Plume & Crest Hair Extensions needs a business card

We need a business card designed for an online luxury hair extensions business called Plume & Crest, we already have a logo and need an innovative business card (2-sided preferably). The strap line for the brand is 'Luxury Hair At Every Touchpoint!'. The brand is a premium brand selling virgin hair extensions and the target market is the mid-affluent ethnic woman as such the design should reflect this. The brand logo is grey and can be sent when requested.

Target Market(s)

25 to 35 year mid-affluent ethnic woman (Afro-American, Mixed Race, Asian)

Industry/Entity Type

Hair

Colors

Designer to choose colors to be used in the design.

Requirements
Must have
• Business Name: Plume and Crest
Strapline: Luxury hair at every touchpoint!
Domain: ​www.plumeandcrest.example
Email: info@plumeandcrest.example
sales and enquiries
44 07500 xxxxxxx

Please use the grey main brand logo depicted in page 2 of the attached pdf document

```html
<!DOCTYPE html>
<html lang="en">
<head>
<meta charset="utf-8">
<title>Plume &amp; Crest Hair Extensions – Business Card</title>
<link href="https://fonts.googleapis.com/css2?family=Didact+Gothic&family=Mulish:wght@800&display=swap" rel="stylesheet">
<style>
  :root {
    --backdrop: #3b8299;
    --card-centre: #ffffff;
    --card-edge: #d6d4d5;
    --ink-grey: #6e6c6d;
    --ink-dark: #4a4849;
    --brand-grey: #9c9a9b;
  }
  html, body {
    margin: 0;
    padding: 0;
    width: 1200px;
    height: 1200px;
    overflow: hidden;
    background: var(--backdrop);
  }
  .canvas {
    position: relative;
    width: 1200px;
    height: 1200px;
  }
  .card {
    position: absolute;
    left: 314px;
    width: 573px;
    height: 318px;
    overflow: hidden;
    font-family: "Didact Gothic", sans-serif;
    color: var(--ink-dark);
  }
  .card--front {
    top: 231px;
    background: radial-gradient(ellipse 75% 80% at 65% 42%, var(--card-centre) 50%, var(--card-edge) 100%);
  }
  .card--back {
    top: 669px;
    background: radial-gradient(ellipse 72% 78% at 50% 45%, var(--card-centre) 50%, var(--card-edge) 100%);
  }

  /* Front */
  .brand {
    position: absolute;
    left: 18px;
    bottom: 40px;
    display: flex;
    align-items: flex-end;
    gap: 18px;
  }
  .brand__mark {
    width: 112px;
    height: 112px;
    background: var(--brand-grey);
  }
  .brand__name {
    font-family: "Didact Gothic", sans-serif;
    font-size: 36px;
    line-height: 1;
    letter-spacing: 1.5px;
    color: var(--brand-grey);
    margin-bottom: -4px;
  }
  .strapline {
    position: absolute;
    left: 296px;
    top: 141px;
    width: 250px;
    margin: 0;
    text-align: center;
    font-family: "Mulish", sans-serif;
    font-weight: 800;
    font-size: 17px;
    line-height: 22px;
    letter-spacing: 0.8px;
    color: var(--ink-grey);
  }

  /* Back */
  .website {
    position: absolute;
    left: 0;
    right: 0;
    top: 130px;
    margin: 0;
    text-align: center;
    font-size: 23px;
    letter-spacing: 1px;
    color: var(--ink-dark);
  }
  .contact {
    position: absolute;
    left: 18px;
    top: 232px;
    margin: 0;
    font-style: normal;
    font-size: 16px;
    line-height: 25px;
    letter-spacing: 0.3px;
    color: var(--ink-dark);
  }
  .contact span { display: block; }
  .contact .contact__email { margin-top: 2px; }
</style>
</head>
<body>
<main class="canvas">
  <section class="card card--front" aria-label="Business card front">
    <div class="brand">
      <span class="brand__mark" aria-hidden="true"></span>
      <span class="brand__name">Plume &amp; Crest</span>
    </div>
    <p class="strapline">Luxury hair at every touchpoint!</p>
  </section>

  <section class="card card--back" aria-label="Business card back">
    <p class="website">www.plumeandcrest.example</p>
    <address class="contact">
      <span>sales and enquiries</span>
      <span>44 07500 xxxxxxx</span>
      <span class="contact__email">info@plumeandcrest.example</span>
    </address>
  </section>
</main>
</body>
</html>
```